Safety Starts at The Top

Want to make a poster showing our company president in full safety gear (see attached photo) encouraging how "Safety Starts at the Top" We encourage creativity. Visit our website for ideas about our company. www.halvorbuilders.com Our main colors are blue and black, but we will allow other colors to make the poster pop and stand out.

Industry/Entity Type

It Company

Colors
0255a3

Requirements
Must have
• -Must have the photo attached somewhere on the poster. Must have a PPE List which can be creative or bullet points 1. Hard Hat 2. Safety Glasses 3. Shirt with Sleeves, 4. Reflective Vest 5. Gloves 6. Long Pants 7. Safety Boots
• -Must have title "Safety Starts at the Top"
• -Must have a box or section that says the following"Because of our company's core value of RESPECT FOR ALL PEOPLE the commitment to Safety Starts at the Top. Marlowe Construction’s most valuable asset is our team members, which is why I take personal responsibility for our safety culture. It is our daily mission for every team member to return home to their families without injuries, giving them a life away from work that can be enjoyed."

```html
<!DOCTYPE html>
<html lang="en">
<head>
<meta charset="utf-8">
<title>Safety Starts at the Top</title>
<link href="https://fonts.googleapis.com/css2?family=Oswald:wght@300;500;600&family=Passion+One:wght@400&display=swap" rel="stylesheet">
<style>
  :root {
    --blue-deep: #23449c;
    --blue-mid: #3a5fb8;
    --rose: #b8678f;
    --violet: #6a4c9c;
    --cream: #fff8dc;
    --title-red: #e0353c;
    --glow: rgba(255, 246, 200, 0.75);
  }
  html, body {
    margin: 0;
    padding: 0;
    width: 849px;
    height: 1200px;
    overflow: hidden;
  }
  .poster {
    position: relative;
    width: 849px;
    height: 1200px;
    overflow: hidden;
    background:
      radial-gradient(ellipse 420px 520px at 120px 820px, rgba(214, 120, 150, 0.85), rgba(214, 120, 150, 0) 70%),
      radial-gradient(ellipse 360px 300px at 200px 1100px, rgba(120, 80, 170, 0.7), rgba(120, 80, 170, 0) 70%),
      radial-gradient(ellipse 500px 500px at 420px 560px, rgba(150, 120, 190, 0.45), rgba(150, 120, 190, 0) 70%),
      linear-gradient(180deg, var(--blue-deep) 0%, var(--blue-mid) 40%, var(--blue-deep) 100%);
    font-family: "Oswald", sans-serif;
    color: var(--cream);
  }
  .title {
    position: absolute;
    top: 14px;
    left: 0;
    width: 849px;
    margin: 0;
    text-align: center;
    font-family: "Passion One", sans-serif;
    font-weight: 400;
    font-size: 82px;
    line-height: 1;
    letter-spacing: 0.5px;
    color: var(--cream);
    text-shadow: -4px -3px 0 var(--title-red), 0 0 14px rgba(255, 255, 255, 0.35);
  }
  .title-rule {
    position: absolute;
    top: 117px;
    left: 38px;
    width: 778px;
    height: 2px;
    background: var(--cream);
    box-shadow: 0 0 6px var(--glow);
  }
  .message {
    position: absolute;
    top: 134px;
    left: 34px;
    width: 783px;
    margin: 0;
    font-weight: 300;
    font-size: 24px;
    line-height: 37.5px;
    text-align: justify;
    text-align-last: left;
    color: var(--cream);
  }
  .president-photo {
    position: absolute;
    left: 60px;
    top: 524px;
    width: 225px;
    height: 568px;
    border-radius: 40px 40px 10px 10px;
    background: linear-gradient(180deg, #2f4f9e 0%, #c9d94a 30%, #c9d94a 45%, #b9a78a 60%, #a89478 92%, #3a3340 100%);
    opacity: 0.9;
  }
  .callouts {
    position: absolute;
    top: 0;
    left: 0;
    filter: drop-shadow(0 0 4px var(--glow));
  }
  .ppe-label {
    position: absolute;
    margin: 0;
    font-weight: 500;
    line-height: 1;
    color: var(--cream);
    text-shadow: 0 0 8px rgba(255, 240, 200, 0.5);
    white-space: nowrap;
  }
  .ppe-hard-hat { left: 331px; top: 450px; font-size: 34px; }
  .ppe-glasses { left: 488px; top: 548px; font-size: 22px; line-height: 27px; text-align: center; }
  .ppe-shirt { left: 544px; top: 658px; font-size: 33px; }
  .ppe-vest { left: 480px; top: 721px; font-size: 30px; }
  .ppe-gloves { left: 589px; top: 770px; font-size: 30px; }
  .ppe-pants { left: 510px; top: 864px; font-size: 38px; }
  .ppe-boots { left: 566px; top: 1043px; font-size: 31px; }
</style>
</head>
<body>
<main class="poster">
  <h1 class="title">Safety Starts at the Top</h1>
  <div class="title-rule"></div>
  <p class="message">Because of our company's core value of RESPECT FOR ALL PEOPLE the commitment to Safety Starts at the Top. Marlowe Construction’s most valuable asset is our team members, which is why I take personal responsibility for our safety culture. It is our daily mission for every team member to return home to their families without injuries, giving them a life away from work that can be enjoyed.</p>

  <div class="president-photo" role="img" aria-label="Photo of the company president standing in full safety gear: blue hard hat, safety glasses, sleeved shirt, yellow reflective vest, gloves, khaki long pants and safety boots"></div>

  <svg class="callouts" width="849" height="1200" viewBox="0 0 849 1200" aria-hidden="true">
    <g fill="none" stroke="#fff8dc" stroke-width="2.5">
      <polyline points="196,538 394,538 394,496"/>
      <line x1="196" y1="576" x2="474" y2="576"/>
      <polyline points="196,620 424,620 424,677 524,677"/>
      <line x1="186" y1="736" x2="458" y2="736"/>
      <line x1="260" y1="784" x2="562" y2="784"/>
      <line x1="244" y1="886" x2="490" y2="886"/>
      <line x1="262" y1="1061" x2="548" y2="1061"/>
    </g>
    <g fill="#fff8dc">
      <circle cx="394" cy="496" r="5.5"/>
      <circle cx="474" cy="576" r="5.5"/>
      <circle cx="524" cy="677" r="5.5"/>
      <circle cx="458" cy="736" r="5.5"/>
      <circle cx="562" cy="784" r="5.5"/>
      <circle cx="490" cy="886" r="5.5"/>
      <circle cx="548" cy="1061" r="5.5"/>
    </g>
  </svg>

  <p class="ppe-label ppe-hard-hat">Hard Hat</p>
  <p class="ppe-label ppe-glasses">Safety<br>Glasses</p>
  <p class="ppe-label ppe-shirt">Shirt with Sleeves</p>
  <p class="ppe-label ppe-vest">Reflective Vest</p>
  <p class="ppe-label ppe-gloves">Gloves</p>
  <p class="ppe-label ppe-pants">Long Pants</p>
  <p class="ppe-label ppe-boots">Safety Boots</p>
</main>
</body>
</html>
```